Bref créative |
Birch Hydraulic | ||
Use same font as used in my logo | ||
Cutting-Edge Corporate Professional Simple |
Paul Destry | ||
Owner | ||
4637 Heron Ridge Lane Clarkston MI 48351 |
destry.paul@mailvane.net | ||

```html
<!DOCTYPE html>
<html lang="en">
<head>
<meta charset="utf-8">
<title>Birch Hydraulic – Business Card</title>
<link rel="stylesheet" href="https://fonts.googleapis.com/css2?family=Arimo:wght@400;700&display=swap">
<style>
  :root {
    --backdrop: #cbcbcb;
    --frame-line: #9a9a9a;
    --green-light: #6cc94f;
    --green-mid: #3fae36;
    --green-deep: #2a9530;
    --brand-green: #1f7a2c;
    --white: #ffffff;
    --ink: #111111;
  }
  * { box-sizing: border-box; margin: 0; padding: 0; }
  html, body { width: 1200px; height: 938px; overflow: hidden; }
  body {
    background: var(--backdrop);
    font-family: "Arimo", Arial, sans-serif;
    color: var(--ink);
    position: relative;
  }
  .backdrop-frame {
    position: absolute;
    left: 20px; top: 20px;
    width: 1160px; height: 898px;
    border: 2px solid var(--frame-line);
  }
  .card {
    position: absolute;
    left: 158px; top: 216px;
    width: 978px; height: 529px;
    background: radial-gradient(ellipse at 55% 45%, var(--green-light) 0%, var(--green-mid) 45%, var(--green-deep) 100%);
  }
  .band {
    position: absolute;
    left: 0; width: 100%;
    background: var(--white);
  }
  .band-top { top: 33px; height: 76px; }
  .band-bottom { top: 440px; height: 46px; }
  .leaf-art {
    position: absolute;
    left: 83px; top: 242px;
    width: 420px; height: 287px;
    background: radial-gradient(ellipse at 50% 40%, rgba(190, 235, 170, 0.45) 0%, rgba(190, 235, 170, 0.15) 55%, rgba(190, 235, 170, 0) 75%);
  }
  .logo-panel {
    position: absolute;
    left: 25px; top: -3px;
    width: 249px; height: 245px;
    background: var(--white);
    border-radius: 26px;
    display: flex;
    flex-direction: column;
    align-items: center;
    justify-content: center;
    gap: 14px;
  }
  .logo-mark {
    width: 58px; height: 58px;
    background: var(--brand-green);
  }
  .logo-name {
    font-weight: 700;
    font-size: 30px;
    line-height: 1.1;
    color: var(--brand-green);
    text-align: center;
  }
  .owner {
    position: absolute;
    right: 15px; top: 50px;
    text-align: right;
  }
  .owner-name { font-size: 36px; line-height: 1.1; }
  .owner-title { font-size: 22px; line-height: 1.2; }
  .owner-cell { font-size: 21px; line-height: 1.2; }
  .contact-panel {
    position: absolute;
    left: 597px; top: 330px;
    width: 363px; height: 178px;
    background: var(--white);
    border-radius: 18px;
    padding: 12px 16px;
    font-size: 23px;
    line-height: 1.17;
  }
  .address { margin-bottom: 8px; }
  .phones { display: grid; grid-template-columns: 70px 24px auto; }
</style>
</head>
<body>
  <div class="backdrop-frame"></div>
  <section class="card">
    <div class="band band-top"></div>
    <div class="band band-bottom"></div>
    <div class="leaf-art" role="img" aria-label="Large soft green leaves decoration"></div>

    <div class="logo-panel">
      <div class="logo-mark"></div>
      <div class="logo-name">Birch<br>Hydraulic</div>
    </div>

    <div class="owner">
      <div class="owner-name">Paul Destry</div>
      <div class="owner-title">Owner</div>
      <div class="owner-cell">Cell : 586-402-1185</div>
    </div>

    <div class="contact-panel">
      <div class="address">
        4637 Heron Ridge Lane<br>
        Clarkston&nbsp; MI&nbsp; 48351<br>
        destry.paul@mailvane.net
      </div>
      <div class="phones">
        <span>Ph</span><span>:</span><span>586-219-4460</span>
        <span>Cell</span><span>:</span><span>586-402-1185</span>
        <span>Fax</span><span>:</span><span>586-219-4463</span>
      </div>
    </div>
  </section>
</body>
</html>
```